Home inspection business! professional look attracting customers just by looks. Read must haves

its a new business I started on my own for home inspections I would like something very professional to give to real estate agents and clients, its going to have my license number on it my business phone number my name my website as well etc on the back side it will be servicing areas and also what kind of services I offer I also have a business card from someone else the way I would like mine to be. I will attach my logo

Home Inspection

listed in nice to haves

• phone number - 555 293 8471
• website- hollowpinecheck.com
• license number #2938475610
• my name Gavin keropulis
• picture of my logo and me on the front
• on the back of the card. stating I am servicing All of New York and Long Island
• also services I will offer will be home inspection -mold inspection -lead inspection -radon inspection -Termite Inspection -Infared Scan.
• and also we provide inspections for single family homes condos co-ops town-homes
• and commercial property
• same colors as the logos and also if you recommend fonts to look like the logo not sure up to you

```html
<!DOCTYPE html>
<html lang="en">
<head>
<meta charset="utf-8">
<title>Hollow Pine Check Home Inspectors – Business Card</title>
<link href="https://fonts.googleapis.com/css2?family=Montserrat:wght@500;600;700&display=swap" rel="stylesheet">
<style>
  :root {
    --backdrop: #e6e2dc;
    --card-grey: #727272;
    --card-white: #ffffff;
    --brand-blue: #3f97d8;
    --band-blue: #52a1dc;
    --text-grey: #5f5f5f;
    --logo-grey: #6a6a6a;
    --white: #ffffff;
  }
  * { box-sizing: border-box; margin: 0; padding: 0; }
  html, body { width: 1200px; height: 900px; overflow: hidden; }
  body {
    background: var(--backdrop);
    font-family: "Montserrat", Arial, sans-serif;
    position: relative;
  }
  .card {
    position: absolute;
    left: 311px;
    width: 577px;
    height: 329px;
    overflow: hidden;
    box-shadow: 0 6px 14px rgba(0,0,0,0.25);
  }
  /* Services side */
  .card--services { top: 98px; background: var(--card-grey); }
  .brand {
    position: absolute;
    text-align: center;
    font-weight: 700;
    line-height: 1.2;
  }
  .card--services .brand {
    left: 0; right: 0; top: 172px;
    color: var(--white);
  }
  .brand__name { font-size: 25px; letter-spacing: 0.5px; display: block; }
  .brand__tag { font-size: 15px; letter-spacing: 4.5px; display: block; }
  .service-list {
    position: absolute;
    left: 0; right: 0; top: 273px;
    text-align: center;
    color: var(--white);
    font-size: 14px;
    font-weight: 500;
    line-height: 17px;
    letter-spacing: 0.2px;
  }
  /* Contact side */
  .card--contact { top: 472px; background: var(--card-white); }
  .portrait {
    position: absolute;
    left: 67px; top: 29px;
    width: 100px; height: 100px;
    border-radius: 50%;
    background: radial-gradient(circle at 50% 35%, #d9c3b0 0 22%, #9aa3ad 23% 60%, #2f3a4c 61%);
  }
  .card--contact .brand {
    left: 318px; top: 82px;
    width: 240px;
    color: var(--logo-grey);
    text-align: left;
  }
  .card--contact .brand__name { font-size: 20px; }
  .card--contact .brand__tag { font-size: 11.5px; letter-spacing: 3.6px; }
  .holder-name {
    position: absolute;
    left: 37px; top: 144px;
    color: var(--brand-blue);
    font-size: 15px;
    font-weight: 600;
    letter-spacing: 0.3px;
  }
  .license {
    position: absolute;
    left: 37px; top: 163px;
    color: var(--text-grey);
    font-size: 14px;
    font-weight: 500;
  }
  .divider {
    position: absolute;
    left: 35px; top: 188px;
    width: 280px; height: 2px;
    background: var(--brand-blue);
  }
  .service-area {
    position: absolute;
    left: 324px; top: 180px;
    color: var(--brand-blue);
    font-size: 13px;
    font-weight: 500;
  }
  .contact-line {
    position: absolute;
    left: 37px;
    display: flex;
    align-items: center;
    gap: 9px;
    color: var(--text-grey);
    font-size: 14px;
    font-weight: 500;
  }
  .contact-line svg { width: 17px; height: 17px; fill: var(--brand-blue); }
  .contact-line--phone { top: 202px; }
  .contact-line--web { top: 225px; }
  .property-band {
    position: absolute;
    left: 0; right: 0; bottom: 0;
    height: 60px;
    background: var(--band-blue);
    color: var(--white);
    font-size: 13px;
    font-weight: 500;
    text-align: center;
    line-height: 18px;
    padding-top: 12px;
    padding-right: 12px;
  }
</style>
</head>
<body>

  <section class="card card--services">
    <div class="brand">
      <span class="brand__name">HOLLOW PINE CHECK</span>
      <span class="brand__tag">HOME INSPECTORS</span>
    </div>
    <p class="service-list">
      HOME INSPECTION • MOLD INSPECTION • LEAD INSPECTION<br>
      RADON INSPECTION • TERMITE INSPECTION • INFARED SCAN
    </p>
  </section>

  <section class="card card--contact">
    <div class="portrait" role="img" aria-label="Portrait photo of the inspector"></div>

    <div class="brand">
      <span class="brand__name">HOLLOW PINE CHECK</span>
      <span class="brand__tag">HOME INSPECTORS</span>
    </div>

    <p class="holder-name">GAVIN KEROPULIS</p>
    <p class="license">LIC NO : #2938475610</p>
    <div class="divider"></div>
    <p class="service-area">All of New York and Long Island</p>

    <p class="contact-line contact-line--phone">
      <svg viewBox="0 0 24 24" aria-hidden="true"><path d="M6.6 10.8a15.1 15.1 0 0 0 6.6 6.6l2.2-2.2c.3-.3.7-.4 1-.2 1.1.4 2.3.6 3.6.6.6 0 1 .4 1 1V20c0 .6-.4 1-1 1A17 17 0 0 1 3 4c0-.6.4-1 1-1h3.5c.6 0 1 .4 1 1 0 1.3.2 2.5.6 3.6.1.3 0 .7-.2 1z"/></svg>
      555 293 8471
    </p>
    <p class="contact-line contact-line--web">
      <svg viewBox="0 0 24 24" aria-hidden="true"><path d="M12 2a10 10 0 1 0 0 20 10 10 0 0 0 0-20zm6.9 6h-2.9a15.7 15.7 0 0 0-1.4-3.6A8 8 0 0 1 18.9 8zM12 4c.8 1.2 1.5 2.5 1.9 4h-3.8c.4-1.5 1.1-2.8 1.9-4zM4.3 14a8.2 8.2 0 0 1 0-4h3.4a16 16 0 0 0 0 4zm.8 2h2.9c.3 1.3.8 2.5 1.4 3.6A8 8 0 0 1 5.1 16zM8 8H5.1a8 8 0 0 1 4.3-3.6C8.8 5.5 8.3 6.7 8 8zm4 12c-.8-1.2-1.5-2.5-1.9-4h3.8c-.4 1.5-1.1 2.8-1.9 4zm2.3-6H9.7a14.7 14.7 0 0 1 0-4h4.6a14.7 14.7 0 0 1 0 4zm.3 5.6c.6-1.1 1.1-2.3 1.4-3.6h2.9a8 8 0 0 1-4.3 3.6zm1.7-5.6a16 16 0 0 0 0-4h3.4a8.2 8.2 0 0 1 0 4z"/></svg>
      www.hollowpinecheck.com
    </p>

    <p class="property-band">
      SINGLE FAMILY HOMES, CONDOS, CO-OPS TOWN-HOMES<br>
      AND COMMERCIA PROPERTY
    </p>
  </section>

</body>
</html>
```